Increasing performance of Security Operations Centers

Stellavant builds Security Operations Centers (SOC) that enable Pinnacle 1000 clients to be proactive and predictive in the way they secure their people and facilities. The methods involve automating threat detection, streamlining workflows, and outsourcing the most appropriate tasks. The outcomes are a reduction in total incidents and faster response times with fewer resources so clients can focus on their core business.
We're looking for 2 slides to replace the attached PPT. The first slide would be broken into each of the 8 capabilities when presenting: i.e. starting with "Reduce incidents..." on the first slide, building on with "Better direct..." on the second and continuing around clockwise. I'm looking for a more compelling way to present the capabilities and am not wedded to the way it is laid out now.
Also attached is our brand book for color and font values to comply with.

I will extend the deadline to 3/28 as soon as I figure out how.

```html
<!DOCTYPE html>
<html lang="en">
<head>
<meta charset="utf-8">
<title>SOC Performance Improvement Objectives</title>
<link href="https://fonts.googleapis.com/css2?family=Arimo:wght@400;700&display=swap" rel="stylesheet">
<style>
  :root {
    --canvas: #bfbfc1;
    --slide: #ffffff;
    --navy: #0b3d64;
    --red: #be2e2a;
    --core: #0f2a48;
    --rule: #eef0f2;
  }
  * { box-sizing: border-box; margin: 0; padding: 0; }
  html, body { width: 960px; height: 1200px; overflow: hidden; }
  body { background: var(--canvas); font-family: "Arimo", Arial, sans-serif; position: relative; }

  .slide { position: absolute; left: 123px; width: 714px; height: 534px; background: var(--slide); overflow: hidden; }
  .slide--wheel { top: 66px; }
  .slide--summary { top: 618px; }

  .slide__title { position: absolute; left: 0; top: 22px; width: 100%; height: 54px; background: var(--navy);
    color: #fff; font-size: 32px; line-height: 54px; padding-left: 35px; letter-spacing: 0.2px; }

  .slide__footer { position: absolute; left: 0; bottom: 0; width: 100%; height: 48px; }
  .brand-name { position: absolute; right: 32px; bottom: 10px; color: #fff; font-size: 29px; line-height: 1; letter-spacing: 0.2px; }

  .wheel { position: absolute; left: 143px; top: 82px; }
  .segment-label { position: absolute; transform: translate(-50%, -50%); color: #fff; text-align: center;
    font-size: 11.5px; line-height: 14px; }
  .segment-label--md { font-size: 12.5px; line-height: 15px; }
  .segment-label--lg { font-size: 16px; line-height: 19px; }

  .headline { position: absolute; left: 0; width: 100%; top: 110px; text-align: center; color: var(--navy);
    font-weight: 700; font-size: 22px; line-height: 27px; }
  .headline em { font-style: normal; color: var(--red); }
  .divider { position: absolute; left: 0; top: 254px; width: 100%; height: 1px; background: var(--rule); }
  .cost-badge { position: absolute; left: 270px; top: 203px; width: 174px; height: 174px; border-radius: 50%;
    background: var(--navy); color: #fff; font-weight: 700; font-size: 21px; line-height: 26px;
    display: flex; align-items: center; justify-content: center; text-align: center; }
  .tagline { position: absolute; left: 0; width: 100%; top: 437px; text-align: center; color: var(--navy);
    font-weight: 700; font-size: 22px; }
</style>
</head>
<body>

<section class="slide slide--wheel">
  <h1 class="slide__title">SOC Performance Improvement Objectives…</h1>

  <svg class="wheel" width="428" height="428" viewBox="-214 -214 428 428" aria-hidden="true">
    <path fill="var(--red)"  d="M0 0 L0 -214 A214 214 0 0 1 151.3 -151.3 Z"/>
    <path fill="var(--navy)" d="M0 0 L151.3 -151.3 A214 214 0 0 1 214 0 Z"/>
    <path fill="var(--red)"  d="M0 0 L214 0 A214 214 0 0 1 151.3 151.3 Z"/>
    <path fill="var(--navy)" d="M0 0 L151.3 151.3 A214 214 0 0 1 0 214 Z"/>
    <path fill="var(--red)"  d="M0 0 L0 214 A214 214 0 0 1 -151.3 151.3 Z"/>
    <path fill="var(--navy)" d="M0 0 L-151.3 151.3 A214 214 0 0 1 -214 0 Z"/>
    <path fill="var(--red)"  d="M0 0 L-214 0 A214 214 0 0 1 -151.3 -151.3 Z"/>
    <path fill="var(--navy)" d="M0 0 L-151.3 -151.3 A214 214 0 0 1 0 -214 Z"/>
    <g stroke="#fff" stroke-width="10">
      <line x1="0" y1="-220" x2="0" y2="220"/>
      <line x1="-220" y1="0" x2="220" y2="0"/>
      <line x1="-156" y1="-156" x2="156" y2="156"/>
      <line x1="156" y1="-156" x2="-156" y2="156"/>
    </g>
    <circle r="94" fill="#fff"/>
    <circle r="78" fill="var(--core)"/>
  </svg>

  <p class="segment-label" style="left:294px; top:147px;">Reduce&nbsp; incidents,<br>respond faster,<br>with fewer<br>resources</p>
  <p class="segment-label" style="left:418px; top:157px;">Better direct<br>your security/safety<br>personnel to<br>situations where<br>they are<br>needed most</p>
  <p class="segment-label" style="left:503px; top:242px;">Free up time for<br>more<br>engagement,<br>deterrence, and<br>investigations.</p>
  <p class="segment-label segment-label--md" style="left:498px; top:353px;">Lessen your<br>management<br>burden</p>
  <p class="segment-label" style="left:411px; top:446px;">Increase your<br>installed systems<br>protective<br>usefulness &amp;<br>adaptability to<br>new threats</p>
  <p class="segment-label" style="left:298px; top:446px;">Automate threat<br>detection,<br>streamline<br>workflows,</p>
  <p class="segment-label segment-label--md" style="left:212px; top:354px;">Outsource Key<br>or Non-Core<br>Functions</p>
  <p class="segment-label segment-label--lg" style="left:213px; top:238px;">Reduce<br>Total Cost</p>

  <svg class="slide__footer" width="714" height="48" viewBox="0 0 714 48" aria-hidden="true">
    <rect x="0" y="36" width="714" height="12" fill="var(--navy)"/>
    <polygon points="457,48 489,0 714,0 714,48" fill="var(--navy)"/>
  </svg>
  <span class="brand-name">stellavant</span>
</section>

<section class="slide slide--summary">
  <h1 class="slide__title">SOC Performance Improvement Objectives…</h1>

  <p class="headline">Reduce&nbsp; <em>Incidents</em>, Respond <em>Faster</em><br>with Fewer <em>Resources</em></p>
  <div class="divider"></div>
  <div class="cost-badge">Reduce Total<br>Cost of<br>Operations</div>
  <p class="tagline">Proactive, Predictive and Preventative</p>

  <svg class="slide__footer" width="714" height="48" viewBox="0 0 714 48" aria-hidden="true">
    <rect x="0" y="36" width="714" height="12" fill="var(--navy)"/>
    <polygon points="457,48 489,0 714,0 714,48" fill="var(--navy)"/>
  </svg>
  <span class="brand-name">stellavant</span>
</section>

</body>
</html>
```